Bold Sparrow Studio
Business Cards, Stationary, T-Shirts
Bold Sparrow Studio -
Creative Brief
Use specific fonts
Feel free to use clear fonts
Bright & Fun-filled
Arch. Dave Tuazon
Business Development Manager
Level C, QRT Business Center 482 Willowgate Street Mandaluyong, Metro Manila
tuazon.ella@brightnestinteriors.com
Okay to use single colors in the background with a different color per sheet. Please make format easily editable to change the names and designations of the people on the business cards
Kitchens Closets Storage Solutions

```html
<!DOCTYPE html>
<html lang="en">
<head>
<meta charset="utf-8">
<title>Brightnest Interiors – Business Card</title>
<link href="https://fonts.googleapis.com/css2?family=Arimo:wght@400;700&display=swap" rel="stylesheet">
<style>
  :root{
    --page-bg:#eeeae4;
    --card-bg:#ffffff;
    --brand-blue:#1a74bd;
    --brand-blue-dark:#0f5c9c;
    --brand-green:#5aa51f;
    --text-dark:#1c1c1c;
    --text-grey:#4a4a4a;
  }
  html,body{margin:0;padding:0;overflow:hidden;}
  body{
    width:1200px;height:965px;
    background:var(--page-bg);
    display:flex;align-items:center;justify-content:center;
    font-family:'Arimo',Arial,sans-serif;
  }
  .business-card{
    position:relative;
    width:1000px;height:528px;
    background:var(--card-bg);
    border-radius:34px;
    overflow:hidden;
    box-shadow:0 6px 18px rgba(0,0,0,.18);
  }
  .card-bands{position:absolute;inset:0;}
  .brand{
    position:absolute;left:50px;top:250px;width:320px;
    display:flex;flex-direction:column;align-items:center;gap:18px;
  }
  .brand-square{width:78px;height:78px;background:var(--brand-blue);border-radius:6px;}
  .brand-name{
    color:var(--brand-blue);font-weight:700;font-size:38px;
    line-height:1.05;text-align:center;letter-spacing:1px;text-transform:uppercase;
  }
  .contact{position:absolute;left:373px;top:88px;color:var(--text-grey);}
  .contact-name{margin:0;color:var(--brand-blue);font-size:44px;font-weight:700;line-height:1.1;}
  .contact-role{margin:6px 0 0;color:var(--text-dark);font-size:24px;font-weight:700;}
  .contact-address{margin:44px 0 0;font-size:23px;line-height:1.38;font-style:normal;}
  .contact-lines{list-style:none;margin:30px 0 0;padding:0;font-size:23px;line-height:1.6;}
  .contact-lines li{display:flex;align-items:center;gap:14px;}
  .contact-lines svg{width:22px;height:22px;fill:var(--brand-blue-dark);flex:none;}
</style>
</head>
<body>
  <article class="business-card">
    <svg class="card-bands" viewBox="0 0 1000 528" preserveAspectRatio="none" aria-hidden="true">
      <defs>
        <linearGradient id="bandBlue" x1="0" y1="0" x2="1" y2="1">
          <stop offset="0" stop-color="#2b8bd6"/>
          <stop offset="1" stop-color="#0f5c9c"/>
        </linearGradient>
      </defs>
      <!-- left band -->
      <path d="M0 0 H128 C70 120 30 300 0 420 Z" fill="var(--brand-green)"/>
      <path d="M0 0 H100 C50 130 20 300 0 400 Z" fill="url(#bandBlue)"/>
      <!-- right band -->
      <path d="M1000 90 C960 250 900 420 840 528 H1000 Z" fill="var(--brand-green)"/>
      <path d="M1000 110 C970 260 920 420 875 528 H1000 Z" fill="url(#bandBlue)"/>
    </svg>

    <div class="brand">
      <span class="brand-square"></span>
      <span class="brand-name">Brightnest Interiors</span>
    </div>

    <section class="contact">
      <h1 class="contact-name">Arch. Dave Tuazon</h1>
      <p class="contact-role">Business Development Manager</p>
      <address class="contact-address">
        Level C, QRT Business Center<br>
        482 Willowgate Street<br>
        Mandaluyong, Metro Manila
      </address>
      <ul class="contact-lines">
        <li><svg viewBox="0 0 24 24"><path d="M6.6 10.8a15 15 0 0 0 6.6 6.6l2.2-2.2c.3-.3.7-.4 1-.2 1.1.4 2.3.6 3.6.6.6 0 1 .4 1 1V20c0 .6-.4 1-1 1A17 17 0 0 1 3 4c0-.6.4-1 1-1h3.5c.6 0 1 .4 1 1 0 1.3.2 2.5.6 3.6.1.3 0 .7-.2 1z"/></svg>(632) 555-0148</li>
        <li><svg viewBox="0 0 24 24"><path d="M6 3h10v5H6zM3 9h18v9h-3v3H6v-3H3zm5 6v4h8v-4z"/></svg>(632) 555-0162</li>
        <li><svg viewBox="0 0 24 24"><path d="M12 2a10 10 0 1 0 5 18.7l-1-1.7A8 8 0 1 1 20 12v1.2c0 1-.7 1.8-1.5 1.8S17 14.2 17 13.2V7h-2v1a5 5 0 1 0 .6 6.6A3.4 3.4 0 0 0 18.5 17c2 0 3.5-1.7 3.5-3.8V12A10 10 0 0 0 12 2zm0 13a3 3 0 1 1 0-6 3 3 0 0 1 0 6z"/></svg>tuazon.ella@brightnestinteriors.com</li>
      </ul>
    </section>
  </article>
</body>
</html>
```